Corrow Family Farm fresh honey jar label

I need a label for jars of honey harvested at our farm. These are for gifts and personal use. We are looking to incorporate our farm brand into the label. We would like the design to take the existing brand and add some element like bees, honey, flowers, or hives to indicate the contents. We want the design to feel homemade and authentic without feeling cheap or hoaky

Requirements
Must have
• The label must be made to fit a 1" x2" rectangular label. The label must include the attached family brand. The label must include the text "Corrow Family Farms" "Pinebrook, USA" "Farm Fresh Honey". The label will be printed on off-white paper
Nice to have
• It would be nice to have illustrations of bees or flowers around the logo or hives or honeycombs. The label should have a vintage feel
Should not have
• The label should not feel overly cartoonish or hoaky

```html
<!DOCTYPE html>
<html lang="en">
<head>
<meta charset="utf-8">
<title>Corrow Family Farms – Farm Fresh Honey Label</title>
<link href="https://fonts.googleapis.com/css2?family=EB+Garamond:wght@500;700&family=Montserrat:wght@300;400&display=swap" rel="stylesheet">
<style>
  :root {
    --backdrop: #bebebe;
    --paper: #f3f3f5;
    --ink: #0b0b0b;
    --rule: #1a1a1a;
    --frame: #7d7d7d;
    --petal: #f39a3c;
    --petal-deep: #e9852a;
    --stem: #8a7d4c;
  }
  html, body {
    margin: 0;
    width: 1200px;
    height: 1200px;
    overflow: hidden;
    background: var(--backdrop);
  }
  .label {
    position: absolute;
    left: 396px;
    top: 193px;
    width: 407px;
    height: 813px;
    background: var(--paper);
    border-radius: 10px;
    color: var(--ink);
  }
  .brand-mark {
    position: absolute;
    left: 0;
    right: 0;
    top: 278px;
    top: 85px;
    text-align: center;
    font-family: "EB Garamond", serif;
    font-weight: 700;
    font-size: 44px;
    line-height: 1.05;
    letter-spacing: 2px;
    color: var(--ink);
  }
  .brand-place {
    position: absolute;
    left: 0;
    right: 0;
    top: 259px;
    text-align: center;
    font-family: "Montserrat", sans-serif;
    font-weight: 400;
    font-size: 16px;
    letter-spacing: 0.5px;
  }
  .divider {
    position: absolute;
    left: 148px;
    top: 322px;
    width: 128px;
    height: 0;
    border-top: 1px solid var(--rule);
  }
  .farm-name {
    position: absolute;
    left: 0;
    right: 0;
    top: 360px;
    text-align: center;
    font-family: "EB Garamond", serif;
    font-weight: 700;
    font-size: 23px;
    letter-spacing: 0.6px;
  }
  .farm-place {
    position: absolute;
    left: 0;
    right: 0;
    top: 397px;
    text-align: center;
    font-family: "EB Garamond", serif;
    font-weight: 500;
    font-size: 17px;
    letter-spacing: 1px;
  }
  .flower-art {
    position: absolute;
    left: 50px;
    top: 459px;
    width: 304px;
    height: 178px;
    background: radial-gradient(ellipse at 50% 35%, var(--petal) 0%, var(--petal-deep) 28%, rgba(243,154,60,0.35) 55%, rgba(138,125,76,0.25) 78%, transparent 100%);
  }
  .product-box {
    position: absolute;
    left: 50px;
    top: 637px;
    width: 302px;
    height: 123px;
    border: 1px solid var(--frame);
    text-align: center;
  }
  .product-kicker {
    margin-top: 18px;
    font-family: "Montserrat", sans-serif;
    font-weight: 300;
    font-size: 27px;
    line-height: 1;
    letter-spacing: 0.5px;
  }
  .product-name {
    margin-top: 4px;
    font-family: "EB Garamond", serif;
    font-weight: 700;
    font-size: 66px;
    line-height: 1;
    letter-spacing: 1px;
  }
</style>
</head>
<body>
  <main class="label">
    <div class="brand-mark">CORROW<br>FAMILY FARM</div>
    <div class="brand-place">PINEBROOK, LOUISIANA</div>
    <div class="divider"></div>
    <div class="farm-name">CORROW FAMILY FARMS</div>
    <div class="farm-place">PINEBROOK, USA</div>
    <div class="flower-art" role="img" aria-label="Illustration of orange wildflowers on slender olive stems with leaves"></div>
    <div class="product-box">
      <div class="product-kicker">FARM FRESH</div>
      <div class="product-name">HONEY</div>
    </div>
  </main>
</body>
</html>
```